Halvik Partners Building Business Cards

We need a business card that reflects our business as "Solar Experts" in San Diego. Browse our website www.halvikpartners.example our License needs to be displayed as "CSLB# 4871306" our phone number is (619) 482-5537

Save thousands on your electric bills and increase the value of your home while helping to protect the environment. Our solar installation experts will help you design the system that's right for you, using only the highest quality equipment that will look great and give you ideal performance. Our goal is to make you energy independent, and get your electric bill to 0.

Paul Ostrander
(619) 482-5537
paul@halvikpartners.example

Target Market(s)

Home owners in san diego looking for solar

Industry/Entity Type

Solar Energy

Contact Information for Business Card

Paul Ostrander
(619) 482-5537
paul@halvikpartners.example

Font styles to use
Other font styles liked:
• Use our logo font

Requirements
Must have
• License needs to be displayed as "CSLB# 4871306" our phone number is (619) 482-5537
Nice to have
• Real images of rooftop home solar in san diego
Should not have
• our business address

```html
<!DOCTYPE html>
<html lang="en">
<head>
<meta charset="utf-8">
<title>Halvik Partners Building – Business Cards</title>
<link rel="stylesheet" href="https://fonts.googleapis.com/css2?family=Merriweather:wght@400;700;900&display=swap">
<style>
  :root {
    --stage: #b9b9b9;
    --card-white: #ffffff;
    --navy: #1f3a7a;
    --navy-deep: #23397a;
    --navy-photo-light: #3f5a9c;
    --gold: #f2ae1c;
    --ink-light: #ffffff;
    --icon-tint: #1f3a7a;
  }
  * { box-sizing: border-box; margin: 0; padding: 0; }
  html, body { width: 1200px; height: 837px; overflow: hidden; }
  body {
    background: var(--stage);
    font-family: "Merriweather", Georgia, serif;
    position: relative;
  }
  .card {
    position: absolute;
    top: 270px;
    width: 520px;
    height: 297px;
    border-radius: 3px;
    box-shadow: 0 10px 24px rgba(0,0,0,0.22);
    overflow: hidden;
  }
  .card--front { left: 50px; background: var(--card-white); }
  .card--back { left: 630px; background: var(--navy-deep); }

  .brand-name {
    font-family: "Merriweather", Georgia, serif;
    font-weight: 900;
    line-height: 1.05;
    text-align: center;
  }
  .card--front .brand-name {
    color: var(--navy);
    font-size: 40px;
    margin-top: 86px;
  }
  .social-row {
    display: flex;
    justify-content: center;
    gap: 10px;
    margin-top: 26px;
  }
  .social-row span {
    width: 20px; height: 20px; border-radius: 2px;
    background: var(--navy);
  }
  .social-row span:nth-child(even) { background: var(--gold); }

  .back-photo {
    position: absolute; inset: 0;
    background: linear-gradient(135deg, var(--navy-photo-light) 0%, var(--navy-deep) 55%, #2a3f80 100%);
  }
  .back-content {
    position: relative;
    padding: 46px 40px 0;
    text-align: center;
    color: var(--ink-light);
  }
  .card--back .brand-name {
    color: var(--ink-light);
    font-size: 30px;
  }
  .contact-name {
    margin-top: 26px;
    font-size: 15px;
    font-weight: 700;
    letter-spacing: 1px;
    text-transform: uppercase;
  }
  .contact-list {
    list-style: none;
    margin-top: 10px;
    font-size: 13px;
    line-height: 1.65;
  }
  .contact-list .accent { color: var(--gold); }
</style>
</head>
<body>
  <section class="card card--front">
    <h1 class="brand-name">Halvik Partners<br>Building</h1>
    <div class="social-row" aria-label="Social profiles">
      <span></span><span></span><span></span><span></span>
    </div>
  </section>

  <section class="card card--back">
    <div class="back-photo" role="img" aria-label="Rooftop solar panels on a home, tinted blue"></div>
    <div class="back-content">
      <h2 class="brand-name">Halvik Partners Building</h2>
      <p class="contact-name">Paul Ostrander</p>
      <ul class="contact-list">
        <li>(619) 482-5537</li>
        <li>paul@halvikpartners.example</li>
        <li>www.<span class="accent">halvikpartners</span>.example</li>
        <li>CSLB# 4871306</li>
      </ul>
    </div>
  </section>
</body>
</html>
```